Design business card using existing logo.

PLEASE DO NOT USE "RED WHITE & BLACK" color combo! Thank you.

Try different color combos such as:
- Vintage colors like brown, orange, gold, blue (not all together but a combo of 1 or 3
- Blue, w/ grey, or silver or white, Blue monochromatic can work as well.
- Use monochromatic variations on back (just an idea)

- Include full name, "Quillmark Records" on at least one side.

Target Market(s)

Teens

Industry/Entity Type

Business

Colors
3277b5
ffc214
f04a50
f78f20

```html
<!DOCTYPE html>
<html lang="en">
<head>
<meta charset="utf-8">
<title>Quillmark Records – Business Card</title>
<link rel="stylesheet" href="https://fonts.googleapis.com/css2?family=Arimo:wght@400;700&display=swap">
<style>
  :root {
    --gold: #fec314;
    --charcoal: #333333;
    --slate: #666666;
    --steel: #999999;
    --mist: #d4d4d4;
    --ink: #111111;
    --white: #ffffff;
    --backdrop: #2a2a2a;
  }
  * { margin: 0; padding: 0; box-sizing: border-box; }
  html, body {
    width: 1200px; height: 1000px; overflow: hidden;
    background: var(--backdrop);
    font-family: "Arimo", Arial, sans-serif;
  }
  .card {
    position: absolute; left: 267px; width: 669px; height: 402px; overflow: hidden;
  }
  .card--front { top: 84px; background: var(--gold); }
  .card--back { top: 526px; background: var(--charcoal); }

  .edge-tab { position: absolute; top: 0; left: 0; }

  .identity {
    position: absolute; left: 35px; top: 58px; width: 300px; text-align: center; color: var(--ink);
    white-space: nowrap;
  }
  .identity__name { font-size: 27px; font-weight: 400; letter-spacing: 0.2px; line-height: 30px; }
  .identity__role { font-size: 13px; line-height: 16px; }

  .logo-slot { position: absolute; left: 95px; top: 126px; }

  .contact-bar {
    position: absolute; left: 347px; width: 322px; height: 52px;
    display: flex; align-items: center; color: var(--white); font-size: 13.5px; line-height: 16px;
    white-space: nowrap;
  }
  .contact-bar svg { position: absolute; left: 18px; }
  .contact-bar__text { margin-left: 64px; }
  .contact-bar--address { top: 61px; background: var(--charcoal); }
  .contact-bar--phone { top: 136px; background: var(--slate); }
  .contact-bar--web { top: 213px; background: var(--steel); color: var(--ink); font-size: 14px; }
  .contact-bar--mail { top: 290px; background: var(--mist); color: var(--ink); font-size: 14px; }

  .brand-frame {
    position: absolute; left: 55px; top: 163px; width: 562px; height: 77px;
    border: 2px solid var(--gold); display: flex; align-items: center; justify-content: center;
    color: var(--white); font-size: 40px; letter-spacing: 0.5px; white-space: nowrap;
  }
</style>
</head>
<body>

<section class="card card--front">
  <svg class="edge-tab" width="30" height="402" viewBox="0 0 30 402">
    <polygon points="0,62 25,87 25,318 0,343" fill="var(--charcoal)"/>
  </svg>

  <div class="identity">
    <div class="identity__name">DARNELL BROOKS</div>
    <div class="identity__role">MANAGING DIRECTOR</div>
  </div>

  <svg class="logo-slot" width="174" height="198" viewBox="0 0 174 198">
    <polygon points="87,1 172,50 172,148 87,197 2,148 2,50" fill="none" stroke="var(--ink)" stroke-width="1.5"/>
    <text x="87" y="94" text-anchor="middle" font-family="Arimo, Arial, sans-serif" font-size="15" fill="var(--ink)">COMPANY</text>
    <text x="87" y="113" text-anchor="middle" font-family="Arimo, Arial, sans-serif" font-size="15" fill="var(--ink)">LOGO</text>
  </svg>

  <div class="contact-bar contact-bar--address">
    <svg width="20" height="30" viewBox="0 0 20 30">
      <path d="M10 1 C4 1 1 5 1 10 C1 16 10 29 10 29 C10 29 19 16 19 10 C19 5 16 1 10 1 Z" fill="var(--steel)"/>
      <circle cx="10" cy="10" r="4.5" fill="var(--white)"/>
    </svg>
    <div class="contact-bar__text">YOUR CITY ADDRESS<br>STREET LOCATION, NY CITY,USA</div>
  </div>

  <div class="contact-bar contact-bar--phone">
    <svg width="22" height="28" viewBox="0 0 22 28">
      <path d="M6 2 L10 8 L7 11 C8 15 11 19 14 21 L17 18 L21 23 L17 26 C10 25 3 15 2 7 Z" fill="none" stroke="var(--white)" stroke-width="2" stroke-linejoin="round"/>
    </svg>
    <div class="contact-bar__text">+18 1234 5678 9012<br>+18 1234 7878 2015</div>
  </div>

  <div class="contact-bar contact-bar--web">
    <svg width="26" height="26" viewBox="0 0 26 26" fill="none" stroke="var(--charcoal)" stroke-width="1.5">
      <circle cx="13" cy="13" r="11"/>
      <ellipse cx="13" cy="13" rx="5" ry="11"/>
      <line x1="2" y1="13" x2="24" y2="13"/>
      <line x1="4" y1="7" x2="22" y2="7"/>
      <line x1="4" y1="19" x2="22" y2="19"/>
    </svg>
    <div class="contact-bar__text">WWW.COMPANYNAME.COM</div>
  </div>

  <div class="contact-bar contact-bar--mail">
    <svg width="30" height="20" viewBox="0 0 30 20">
      <rect x="0" y="0" width="30" height="20" fill="var(--ink)"/>
      <polyline points="1,1 15,11 29,1" fill="none" stroke="var(--mist)" stroke-width="1.5"/>
      <line x1="1" y1="19" x2="11" y2="9" stroke="var(--mist)" stroke-width="1.5"/>
      <line x1="29" y1="19" x2="19" y2="9" stroke="var(--mist)" stroke-width="1.5"/>
    </svg>
    <div class="contact-bar__text">info@companyname.com</div>
  </div>
</section>

<section class="card card--back">
  <svg class="edge-tab" width="669" height="402" viewBox="0 0 669 402">
    <polygon points="0,61 28,88 28,314 0,341" fill="var(--gold)"/>
    <polygon points="669,61 641,88 641,314 669,341" fill="var(--gold)"/>
  </svg>
  <div class="brand-frame">QUILLMARK RECORDS</div>
</section>

</body>
</html>
```